New Flyer Design Project

Hi,
We were looking at a flyer for the testing run of the event. I have attached a design we like with comments on what to remove and add. Also attached is our logo. We want something with the same style and feel of the flyer attached and it suited the event we are running.
Thanks,
Colin
Colors
Designer to choose colors to be used in the design.

```html
<!DOCTYPE html>
<html lang="en">
<head>
<meta charset="utf-8">
<title>The Steel Stallion – Test Runners Required</title>
<link href="https://fonts.googleapis.com/css2?family=Oswald:wght@500;600;700&family=Roboto:wght@400;500&display=swap" rel="stylesheet">
<style>
  :root {
    --paper: #f1ece4;
    --haze: #d8d2c7;
    --rock: #8c8a83;
    --earth: #7b5d41;
    --soil: #553e2c;
    --frame-blue: #3f6f8e;
    --ink: #2b2b2d;
    --orange: #e2763a;
    --white: #ffffff;
  }
  * { margin: 0; padding: 0; box-sizing: border-box; }
  html, body { width: 849px; height: 1200px; overflow: hidden; background: var(--paper); }
  .poster {
    position: relative;
    width: 849px;
    height: 1200px;
    overflow: hidden;
    font-family: "Oswald", sans-serif;
  }
  .mountain-scene {
    position: absolute;
    inset: 0;
    background: linear-gradient(180deg,
      var(--paper) 0%,
      var(--paper) 30%,
      var(--haze) 44%,
      var(--rock) 58%,
      var(--earth) 76%,
      var(--soil) 100%);
  }
  .frame { position: absolute; inset: 0; }
  .social-row {
    position: absolute;
    top: 70px;
    left: 0;
    width: 100%;
    display: flex;
    justify-content: center;
    gap: 70px;
    font-family: "Roboto", sans-serif;
    font-weight: 500;
    font-size: 24px;
    color: var(--ink);
  }
  .social-handle { display: flex; align-items: center; gap: 12px; }
  .social-dot {
    width: 22px; height: 22px;
    border-radius: 50%;
    background: var(--ink);
  }
  .brand {
    position: absolute;
    top: 250px;
    left: 0;
    width: 100%;
    text-align: center;
    color: var(--ink);
  }
  .brand-name {
    display: inline-block;
    font-weight: 600;
    font-size: 86px;
    letter-spacing: 8px;
    line-height: 1.05;
    text-transform: uppercase;
    padding: 14px 0;
    border-top: 3px solid var(--ink);
    border-bottom: 3px solid var(--ink);
  }
  .brand-name .brand-article { display: block; font-size: 62px; letter-spacing: 14px; }
  .banner {
    position: absolute;
    left: 50%;
    transform: translateX(-50%);
    background: var(--orange);
    color: var(--white);
    font-weight: 600;
    text-transform: uppercase;
    white-space: nowrap;
    text-align: center;
  }
  .banner-headline {
    top: 580px;
    padding: 10px 28px;
    font-size: 48px;
    line-height: 58px;
  }
  .event-date {
    position: absolute;
    top: 700px;
    left: 0;
    width: 100%;
    text-align: center;
    color: var(--white);
    font-weight: 700;
    font-size: 72px;
    line-height: 84px;
    letter-spacing: 1px;
  }
  .banner-venue {
    top: 808px;
    padding: 8px 60px;
    font-size: 46px;
    line-height: 60px;
    clip-path: polygon(4% 0, 100% 0, 96% 50%, 100% 100%, 0 100%, 4% 50%, 0 0);
    clip-path: polygon(0 0, 100% 0, 96% 50%, 100% 100%, 0 100%, 4% 50%);
  }
  .contact {
    position: absolute;
    top: 1000px;
    left: 0;
    width: 100%;
    text-align: center;
    color: var(--white);
    font-family: "Roboto", sans-serif;
    font-size: 23px;
    line-height: 30px;
  }
</style>
</head>
<body>
  <main class="poster">
    <div class="mountain-scene" role="img" aria-label="Photograph of a runner standing on a rocky alpine ridge above hazy mountain valleys"></div>

    <svg class="frame" width="849" height="1200" viewBox="0 0 849 1200" aria-hidden="true">
      <polyline points="64,820 64,128 786,128 786,430" fill="none" stroke="var(--frame-blue)" stroke-width="10"/>
    </svg>

    <div class="social-row">
      <span class="social-handle"><span class="social-dot"></span>@STEELSTALLIONRACE</span>
      <span class="social-handle"><span class="social-dot"></span>@THESTEELSTALLIONRACE</span>
    </div>

    <div class="brand">
      <h1 class="brand-name"><span class="brand-article">The</span>Steel Stallion</h1>
    </div>

    <p class="banner banner-headline">Test Runners Required</p>

    <p class="event-date">15TH DECEMBER 2019</p>

    <p class="banner banner-venue">At Mount Kalora</p>

    <p class="contact">Contact us steelstallionrace@mailbox.com<br>or call 0400555128</p>
  </main>
</body>
</html>
```